Massage-Creme label for a young pharmacy

We are a young pharmacy which is part of a big union. We developed for a customer a very good massage creme with aloe vera, coconut oil, and many more advantages and as well a massage jelly. All we need is a good and affordable label which is beatiful and helps us to promote our product. As we want to develop further products, it would be very cool to have a corporate label for all upcoming products.

Target Market(s)

professional masseurs and physiotherapists

Industry/Entity Type

Health And Wellness

Font styles to use
Sans Serif
Decorative

Colors

Designer to choose colors to be used in the design.

Requirements
Must have
• Professionally looking design (but I'm sure you are doing so... :-)
Nice to have
• Label can have any shape. What you see is just a bad label with corresponding sizes, so you can imagine how it would look like in the final state.
Should not have
• If possible, the label should not be completely black (although it might look cool) as we are printing it on our own Vostek qr318-ux and black is difficult to print (and very costy).

```html
<!DOCTYPE html>
<html lang="de">
<head>
<meta charset="utf-8">
<title>Massage-Creme Etikett</title>
<link rel="stylesheet" href="https://fonts.googleapis.com/css2?family=Kalam:wght@700&family=Nunito:wght@600;700&family=Arimo:wght@400;700&display=swap">
<style>
  :root {
    --green-top: #b2f0a0;
    --green-mid: #d6f7cc;
    --green-soft: #ecfbe7;
    --pill-green: #c9f2bc;
    --deep-green: #0f3d12;
    --brown: #4a2a10;
    --red: #e0102a;
    --ink: #2b2b2b;
    --white: #ffffff;
  }
  * { box-sizing: border-box; margin: 0; padding: 0; }
  html, body { width: 1200px; height: 1033px; overflow: hidden; background: var(--white); }
  body { position: relative; font-family: "Arimo", Arial, sans-serif; }

  .label {
    position: absolute;
    overflow: hidden;
    background: linear-gradient(180deg, var(--green-top) 0%, var(--green-mid) 45%, var(--green-soft) 100%);
  }
  .label--spread { left: 12px; top: 231px; width: 711px; height: 566px; }
  .label--front  { left: 757px; top: 260px; width: 420px; height: 669px; }

  .waves { position: absolute; inset: 0; width: 100%; height: 100%; }

  .brand-pill {
    position: absolute;
    border-radius: 40px;
    background: linear-gradient(90deg, #d4d4d4, #f6f6f6 50%, #d8d8d8);
    display: flex; flex-direction: column; align-items: center; justify-content: center;
  }
  .brand-pill__name {
    font-family: "Arimo", Arial, sans-serif; font-weight: 700; color: var(--red);
    letter-spacing: 2px;
  }
  .brand-pill__sub {
    font-weight: 700; color: #555; letter-spacing: 1px; text-transform: uppercase;
  }

  .product-title {
    position: absolute;
    font-family: "Kalam", "Comic Sans MS", cursive;
    font-weight: 700; color: var(--deep-green);
    line-height: 1; white-space: nowrap;
  }
  .product-title--spread { left: 42px; top: 112px; font-size: 41px; }
  .product-title--front  { left: 46px; top: 132px; font-size: 48px; }

  .claim {
    position: absolute;
    background: var(--white);
    border-radius: 18px;
    font-family: "Nunito", Arial, sans-serif; font-weight: 700;
    color: var(--red); line-height: 1.15;
    padding: 3px 14px;
  }
  .variant {
    position: absolute;
    background: var(--pill-green);
    border-radius: 24px;
    font-family: "Nunito", Arial, sans-serif; font-weight: 700;
    color: var(--brown);
    display: flex; align-items: center; justify-content: center;
    white-space: nowrap;
  }
  .artwork {
    position: absolute;
    border-radius: 40% 40% 30% 30%;
    background: radial-gradient(ellipse at 50% 60%, #8b5a2b 0%, #2f8f2a 35%, #9fe08f 70%, rgba(200,240,190,0) 100%);
  }
  .volume {
    position: absolute;
    background: var(--pill-green);
    border-radius: 14px;
    color: var(--ink);
    display: flex; align-items: center; justify-content: center;
  }

  .copy {
    position: absolute; left: 417px; top: 62px; width: 230px;
    text-align: center; color: var(--ink); font-size: 9.4px; line-height: 1.3;
  }
  .copy p { margin-bottom: 11px; }
  .copy .ph-note { color: #888; }
  .ph-rule { position: absolute; left: 440px; top: 223px; width: 186px; height: 1px; background: var(--ink); }
  .ph-rule::after { content: ""; position: absolute; left: 90px; top: -2px; width: 4px; height: 4px; border: 1px solid var(--ink); border-radius: 50%; background: var(--white); }
  .quality-note { position: absolute; left: 417px; top: 250px; width: 230px; text-align: center; font-size: 7px; color: #666; line-height: 1.3; }
  .free-from {
    position: absolute; left: 427px; top: 284px; width: 213px; height: 44px;
    border: 3px solid #111; background: var(--white);
    font-size: 7px; text-align: center; line-height: 1.3; color: var(--ink);
    display: flex; align-items: center; justify-content: center; padding: 0 6px;
  }
  .maker { position: absolute; left: 528px; top: 440px; }
  .maker__name { font-size: 10px; font-weight: 700; color: var(--red); letter-spacing: 1.5px; }
  .maker__sub { font-size: 5px; background: #555; color: var(--white); padding: 1px 4px; border-radius: 4px; display: inline-block; }
  .maker__addr { position: absolute; left: 564px; top: 467px; font-size: 5.5px; color: #e8f8e2; line-height: 1.25; }
  .batch { position: absolute; left: 418px; top: 477px; font-size: 6.5px; color: var(--ink); line-height: 1.25; }
  .ingredients { position: absolute; left: 418px; top: 503px; width: 230px; font-size: 5.6px; color: #555; line-height: 1.35; }
  .back-volume { position: absolute; left: 516px; top: 538px; font-size: 12px; color: var(--ink); }
</style>
</head>
<body>

<section class="label label--spread">
  <svg class="waves" viewBox="0 0 711 566" preserveAspectRatio="none" aria-hidden="true">
    <path d="M0 180 C160 230 300 300 711 360" stroke="#fff" stroke-width="3" fill="none" opacity=".9"/>
    <path d="M0 330 C200 420 360 470 711 410" stroke="#fff" stroke-width="14" fill="none" opacity=".35"/>
    <path d="M0 500 C220 520 460 410 711 300" stroke="#fff" stroke-width="2" fill="none" opacity=".9"/>
    <path d="M300 420 C420 360 560 330 711 298" stroke="#5fd33a" stroke-width="2" fill="none"/>
  </svg>

  <div class="brand-pill" style="left:9px;top:32px;width:337px;height:50px;">
    <span class="brand-pill__name" style="font-size:16px;">verdalis</span>
    <span class="brand-pill__sub" style="font-size:6px;">Apotheke Dr. Lindqvist · Drogerie &amp; Parfumerie</span>
  </div>
  <h1 class="product-title product-title--spread">Massage-Creme</h1>
  <div class="claim" style="left:212px;top:165px;font-size:15px;">energetisch<br>leitend!</div>
  <div class="variant" style="left:66px;top:238px;width:280px;height:38px;font-size:23px;">ALOE VERA | COCONUT</div>
  <div class="artwork" style="left:23px;top:276px;width:330px;height:230px;" role="img" aria-label="Aloe-Vera-Blätter mit halbierter Kokosnuss und goldenem Öltropfen"></div>
  <div class="volume" style="left:123px;top:524px;width:109px;height:24px;font-size:17px;">e 1000ml</div>

  <div class="copy">
    <p>Hochwertige und sehr hautschonende Emulsion mit hervorragendem Gleitverhalten für die professionelle Massage.</p>
    <p>Hilft durch den hohen Gehalt an Aloe Vera-Gel (50%), die Feuchtigkeit der Haut zu erhalten und schützt durch die Zugabe von Panthenol (= Provitamin B5) und Allantoin vor Hautreizungen.</p>
    <p>Speziell für die (bio-)energetische Massage entwickelt.</p>
    <p>pH-neutral für die Haut <span class="ph-note">(pH-Wert = 5.5)</span></p>
  </div>
  <div class="ph-rule"></div>
  <p class="quality-note">Bei der Entwicklung unserer Produkte legen wir grössten Wert auf gute Verträglichkeit und hochwertige Rohstoffe.</p>
  <p class="free-from">Dieses Produkt ist frei von Parabenen, Mineralölen (Paraffin/Vaseline), Silikonen, Farbstoffen und Mikroplastik (Acrylate).</p>

  <div class="maker">
    <div class="maker__name">verdalis</div>
    <div class="maker__sub">Apotheke Dr. Lindqvist</div>
  </div>
  <p class="maker__addr">Hauptstrasse 12, 4000 Musterstadt<br>Telefon 000 000 00 00<br>info@verdalis-apotheke.example</p>
  <p class="batch">Exp: 03/2021<br>Lot: 913015/A</p>
  <p class="ingredients">Zus.: water (aqua), cetearyl isononanoate, ethylhexyl stearate, cocos nucifera (coconut oil), octyldodecanol, glycerol, glyceryl stearate citrate, cetearyl alcohol, phenoxyethanol (and) caprylyl glycol, panthenol, sodium chloride, xanthan gum, disodium hydrogenphosphate, citric acid, aloe barbadensis leaf juice extract, allantoin, parfum</p>
  <p class="back-volume">e 1000 ml</p>
</section>

<section class="label label--front">
  <svg class="waves" viewBox="0 0 420 669" preserveAspectRatio="none" aria-hidden="true">
    <path d="M0 240 C120 270 260 330 420 380" stroke="#fff" stroke-width="3" fill="none" opacity=".9"/>
    <path d="M0 400 C150 470 280 520 420 470" stroke="#fff" stroke-width="16" fill="none" opacity=".35"/>
    <path d="M0 625 C160 630 300 560 420 500" stroke="#fff" stroke-width="2" fill="none" opacity=".9"/>
    <path d="M200 560 C280 520 350 500 420 480" stroke="#5fd33a" stroke-width="2" fill="none"/>
  </svg>

  <div class="brand-pill" style="left:12px;top:36px;width:397px;height:60px;">
    <span class="brand-pill__name" style="font-size:19px;">verdalis</span>
    <span class="brand-pill__sub" style="font-size:7px;">Apotheke Dr. Lindqvist · Drogerie &amp; Parfumerie</span>
  </div>
  <h2 class="product-title product-title--front">Massage-Creme</h2>
  <div class="claim" style="left:252px;top:196px;font-size:17px;padding:4px 16px;">energetisch<br>leitend!</div>
  <div class="variant" style="left:78px;top:279px;width:330px;height:47px;font-size:27px;">ALOE VERA | COCONUT</div>
  <div class="artwork" style="left:7px;top:326px;width:413px;height:266px;" role="img" aria-label="Aloe-Vera-Blätter mit halbierter Kokosnuss und goldenem Öltropfen"></div>
  <div class="volume" style="left:146px;top:621px;width:128px;height:27px;font-size:20px;">e 1000ml</div>
</section>

</body>
</html>
```